Audio Spectrum Infographic

We need an infographic similar to the attached for an online course. There are a few changes but we are generally looking for better colors and a less cluttered design with more clarity.

For the types (Vocals -Harp) we would like to include as many as possible without the clutter. Better fonts and non-distracting background colors will help.

The Sound Effects section (Rumble, Tinny, etc) needs to stay but perhaps more buttons and less lines. We would like it to be easy to read and less cluttered.

The "DKV 1/3rd octave Equalizer Bands" and wave image can be removed.

The Sub Bass, Bass, Midrange, High Mids, High Frequency information needs to stay.

We will have other graphics to complete once this is completed.

```html
<!DOCTYPE html>
<html lang="en">
<head>
<meta charset="utf-8">
<title>Audio Spectrum Infographic</title>
<link href="https://fonts.googleapis.com/css2?family=Roboto+Condensed:wght@400;700&display=swap" rel="stylesheet">
<style>
  :root{
    --rail:#262626;
    --zone-sub:#3a3a3a;
    --zone-bass:#505050;
    --zone-mid:#686868;
    --zone-himid:#838383;
    --zone-high:#9c9c9c;
    --zone-high-end:#b4b4b4;
    --bar-low:#ec4420;
    --bar-high:#f6ea6a;
    --bar-ext:#1c1c1c;
    --pill-a:#c8381f;
    --pill-b:#6a1a0f;
    --keys-light:#f4f4f4;
    --keys-shade:#c9c9c9;
    --text:#ffffff;
    --rule:rgba(255,255,255,.55);
    --grid:rgba(255,255,255,.13);
  }
  html,body{margin:0;padding:0;width:1200px;height:943px;overflow:hidden;background:var(--rail);}
  svg.spectrum{display:block;width:1200px;height:943px;font-family:"Roboto Condensed",Arial,sans-serif;}
  .axis-label{fill:var(--text);font-size:11px;text-anchor:middle;}
  .axis-unit{fill:var(--text);font-size:11px;font-weight:700;text-anchor:middle;}
  .section-label{fill:var(--text);font-size:12px;font-weight:700;text-anchor:middle;}
  .instrument{fill:var(--text);font-size:12.5px;font-weight:700;text-anchor:end;}
  .instrument.after{text-anchor:start;}
  .bar-low{fill:var(--bar-low);}
  .bar-high{fill:var(--bar-high);}
  .bar-ext{fill:var(--bar-ext);}
  .grid-line{stroke:var(--grid);stroke-width:1;}
  .rule{stroke:var(--rule);stroke-width:1;}
  .piano-title{fill:var(--text);font-size:11.5px;font-weight:700;text-anchor:middle;}
  .bracket{fill:none;stroke:#c23a22;stroke-width:1;}
  .keyboard{fill:url(#keysFill);}
  .marker{stroke:#d8452a;stroke-width:1.5;}
  .marker-label{fill:var(--text);font-size:10.5px;text-anchor:middle;}
  .pill rect{fill:url(#pillFill);}
  .pill text{fill:var(--text);font-size:10.5px;text-anchor:middle;}
  .pill.small text{font-size:8px;}
  .band-name{fill:var(--text);font-size:12.5px;font-weight:700;text-anchor:middle;}
</style>
</head>
<body>
<svg class="spectrum" viewBox="0 0 993 780" xmlns="http://www.w3.org/2000/svg">
  <defs>
    <linearGradient id="highFill" x1="0" x2="1">
      <stop offset="0" stop-color="var(--zone-high)"/>
      <stop offset="1" stop-color="var(--zone-high-end)"/>
    </linearGradient>
    <linearGradient id="pillFill" x1="0" x2="1">
      <stop offset="0" stop-color="var(--pill-a)"/>
      <stop offset="1" stop-color="var(--pill-b)"/>
    </linearGradient>
    <linearGradient id="keysFill" x1="0" x2="0" y1="0" y2="1">
      <stop offset="0" stop-color="var(--keys-light)"/>
      <stop offset="1" stop-color="var(--keys-shade)"/>
    </linearGradient>
  </defs>

  <g class="zones">
    <rect x="0" y="0" width="35" height="780" fill="var(--rail)"/>
    <rect x="35" y="0" width="181" height="780" fill="var(--zone-sub)"/>
    <rect x="216" y="0" width="186" height="780" fill="var(--zone-bass)"/>
    <rect x="402" y="0" width="274" height="780" fill="var(--zone-mid)"/>
    <rect x="676" y="0" width="142" height="780" fill="var(--zone-himid)"/>
    <rect x="818" y="0" width="175" height="780" fill="url(#highFill)"/>
  </g>

  <g class="grid">
    <line class="grid-line" x1="65" y1="30" x2="65" y2="518"/>
    <line class="grid-line" x1="165" y1="30" x2="165" y2="518"/>
    <line class="grid-line" x1="212" y1="30" x2="212" y2="518"/>
    <line class="grid-line" x1="283" y1="30" x2="283" y2="518"/>
    <line class="grid-line" x1="360" y1="30" x2="360" y2="518"/>
    <line class="grid-line" x1="464" y1="30" x2="464" y2="518"/>
    <line class="grid-line" x1="517" y1="30" x2="517" y2="518"/>
    <line class="grid-line" x1="585" y1="30" x2="585" y2="518"/>
    <line class="grid-line" x1="679" y1="30" x2="679" y2="518"/>
    <line class="grid-line" x1="767" y1="30" x2="767" y2="518"/>
    <line class="grid-line" x1="818" y1="30" x2="818" y2="518"/>
    <line class="grid-line" x1="882" y1="30" x2="882" y2="518"/>
    <line class="grid-line" x1="940" y1="30" x2="940" y2="518"/>
    <line class="grid-line" x1="972" y1="30" x2="972" y2="518"/>
  </g>

  <g class="axis top">
    <text class="axis-unit" x="18" y="22">Hz</text>
    <text class="axis-label" x="65" y="22">20</text>
    <text class="axis-label" x="165" y="22">40</text>
    <text class="axis-label" x="212" y="22">60</text>
    <text class="axis-label" x="283" y="22">100</text>
    <text class="axis-label" x="360" y="22">200</text>
    <text class="axis-label" x="464" y="22">400</text>
    <text class="axis-label" x="517" y="22">600</text>
    <text class="axis-label" x="585" y="22">1K</text>
    <text class="axis-label" x="679" y="22">2K</text>
    <text class="axis-label" x="767" y="22">4K</text>
    <text class="axis-label" x="818" y="22">6K</text>
    <text class="axis-label" x="882" y="22">10K</text>
    <text class="axis-label" x="940" y="22">16K</text>
    <text class="axis-label" x="972" y="22">20K</text>
  </g>

  <g class="rules">
    <line class="rule" x1="0" y1="30" x2="993" y2="30"/>
    <line class="rule" x1="0" y1="72" x2="993" y2="72" opacity=".5"/>
    <line class="rule" x1="0" y1="177" x2="993" y2="177" opacity=".5"/>
    <line class="rule" x1="0" y1="262" x2="993" y2="262" opacity=".5"/>
    <line class="rule" x1="0" y1="396" x2="993" y2="396" opacity=".5"/>
    <line class="rule" x1="0" y1="518" x2="993" y2="518" opacity=".5"/>
    <line class="rule" x1="35" y1="30" x2="35" y2="752"/>
  </g>

  <g class="sections">
    <text class="section-label" transform="translate(22 51) rotate(90)">Vocal</text>
    <text class="section-label" transform="translate(22 124) rotate(90)">Percussion</text>
    <text class="section-label" transform="translate(22 219) rotate(90)">Brass</text>
    <text class="section-label" transform="translate(22 329) rotate(90)">Woodwinds</text>
    <text class="section-label" transform="translate(22 457) rotate(90)">Strings</text>
  </g>

  <g class="instrument-row"><text class="instrument" x="278" y="48">Male</text>
    <rect class="bar-high" x="571" y="41.5" width="374" height="5" rx="2.5"/><rect class="bar-low" x="283" y="41.5" width="290" height="5" rx="2.5"/><rect class="bar-ext" x="860" y="42" width="84" height="4" rx="2"/></g>
  <g class="instrument-row"><text class="instrument" x="392" y="64">Female</text>
    <rect class="bar-high" x="590" y="57.5" width="355" height="5" rx="2.5"/><rect class="bar-low" x="400" y="57.5" width="192" height="5" rx="2.5"/><rect class="bar-ext" x="860" y="58" width="84" height="4" rx="2"/></g>

  <g class="instrument-row"><text class="instrument" x="143" y="91">Kick</text>
    <rect class="bar-high" x="490" y="84.5" width="362" height="5" rx="2.5"/><rect class="bar-low" x="192" y="84.5" width="300" height="5" rx="2.5"/></g>
  <g class="instrument-row"><text class="instrument" x="195" y="106">Tympany</text>
    <rect class="bar-high" x="530" y="99.5" width="198" height="5" rx="2.5"/><rect class="bar-low" x="218" y="99.5" width="314" height="5" rx="2.5"/></g>
  <g class="instrument-row"><text class="instrument" x="225" y="121">Toms</text>
    <rect class="bar-high" x="490" y="114.5" width="352" height="5" rx="2.5"/><rect class="bar-low" x="235" y="114.5" width="257" height="5" rx="2.5"/></g>
  <g class="instrument-row"><text class="instrument" x="258" y="136">Snare</text>
    <rect class="bar-high" x="400" y="129.5" width="482" height="5" rx="2.5"/><rect class="bar-low" x="283" y="129.5" width="119" height="5" rx="2.5"/></g>
  <g class="instrument-row"><text class="instrument" x="299" y="152">Congas</text>
    <rect class="bar-high" x="578" y="145.5" width="219" height="5" rx="2.5"/><rect class="bar-low" x="335" y="145.5" width="245" height="5" rx="2.5"/></g>
  <g class="instrument-row"><text class="instrument" x="347" y="167">Cymbals</text>
    <rect class="bar-high" x="571" y="160.5" width="366" height="5" rx="2.5"/><rect class="bar-low" x="355" y="160.5" width="218" height="5" rx="2.5"/><rect class="bar-ext" x="356" y="161" width="71" height="4" rx="2"/></g>

  <g class="instrument-row"><text class="instrument" x="76" y="193">Tuba</text>
    <rect class="bar-high" x="453" y="186.5" width="225" height="5" rx="2.5"/><rect class="bar-low" x="122" y="186.5" width="333" height="5" rx="2.5"/><rect class="bar-ext" x="123" y="187" width="53" height="4" rx="2"/></g>
  <g class="instrument-row"><text class="instrument" x="144" y="208">French Horn</text>
    <rect class="bar-high" x="556" y="201.5" width="241" height="5" rx="2.5"/><rect class="bar-low" x="210" y="201.5" width="348" height="5" rx="2.5"/><rect class="bar-ext" x="211" y="202" width="23" height="4" rx="2"/></g>
  <g class="instrument-row"><text class="instrument" x="201" y="223">Bass Trombone</text>
    <rect class="bar-high" x="464" y="216.5" width="414" height="5" rx="2.5"/><rect class="bar-low" x="213" y="216.5" width="253" height="5" rx="2.5"/><rect class="bar-ext" x="795" y="217" width="82" height="4" rx="2"/></g>
  <g class="instrument-row"><text class="instrument" x="257" y="239">Tenor Trombone</text>
    <rect class="bar-high" x="498" y="232.5" width="387" height="5" rx="2.5"/><rect class="bar-low" x="258" y="232.5" width="242" height="5" rx="2.5"/><rect class="bar-ext" x="800" y="233" width="84" height="4" rx="2"/></g>
  <g class="instrument-row"><text class="instrument" x="330" y="254">Trumpet</text>
    <rect class="bar-high" x="608" y="247.5" width="266" height="5" rx="2.5"/><rect class="bar-low" x="343" y="247.5" width="267" height="5" rx="2.5"/></g>

  <g class="instrument-row"><text class="instrument after" x="786" y="280">Contrabassoon</text>
    <rect class="bar-high" x="363" y="273.5" width="400" height="5" rx="2.5"/><rect class="bar-low" x="102" y="273.5" width="263" height="5" rx="2.5"/></g>
  <g class="instrument-row"><text class="instrument" x="166" y="296">Bassoon</text>
    <rect class="bar-high" x="525" y="289.5" width="347" height="5" rx="2.5"/><rect class="bar-low" x="208" y="289.5" width="319" height="5" rx="2.5"/></g>
  <g class="instrument-row"><text class="instrument" x="222" y="311">Tenor Sax</text>
    <rect class="bar-high" x="538" y="304.5" width="387" height="5" rx="2.5"/><rect class="bar-low" x="300" y="304.5" width="240" height="5" rx="2.5"/><rect class="bar-ext" x="860" y="305" width="64" height="4" rx="2"/></g>
  <g class="instrument-row"><text class="instrument" x="267" y="326">Alto Sax</text>
    <rect class="bar-high" x="545" y="319.5" width="380" height="5" rx="2.5"/><rect class="bar-low" x="317" y="319.5" width="230" height="5" rx="2.5"/><rect class="bar-ext" x="860" y="320" width="64" height="4" rx="2"/></g>
  <g class="instrument-row"><text class="instrument" x="309" y="342">Clarinet</text>
    <rect class="bar-high" x="681" y="335.5" width="234" height="5" rx="2.5"/><rect class="bar-low" x="317" y="335.5" width="366" height="5" rx="2.5"/></g>
  <g class="instrument-row"><text class="instrument" x="355" y="357">Oboe</text>
    <rect class="bar-high" x="649" y="350.5" width="266" height="5" rx="2.5"/><rect class="bar-low" x="388" y="350.5" width="263" height="5" rx="2.5"/></g>
  <g class="instrument-row"><text class="instrument" x="388" y="373">Flute</text>
    <rect class="bar-high" x="686" y="366.5" width="217" height="5" rx="2.5"/><rect class="bar-low" x="402" y="366.5" width="286" height="5" rx="2.5"/></g>
  <g class="instrument-row"><text class="instrument" x="492" y="388">Piccolo</text>
    <rect class="bar-high" x="762" y="381.5" width="159" height="5" rx="2.5"/><rect class="bar-low" x="519" y="381.5" width="245" height="5" rx="2.5"/></g>

  <g class="instrument-row"><text class="instrument" x="105" y="414">Bass</text>
    <rect class="bar-high" x="443" y="407.5" width="354" height="5" rx="2.5"/><rect class="bar-low" x="122" y="407.5" width="323" height="5" rx="2.5"/><rect class="bar-ext" x="123" y="408" width="39" height="4" rx="2"/></g>
  <g class="instrument-row"><text class="instrument" x="210" y="429">Cello</text>
    <rect class="bar-high" x="497" y="422.5" width="351" height="5" rx="2.5"/><rect class="bar-low" x="224" y="422.5" width="275" height="5" rx="2.5"/></g>
  <g class="instrument-row"><text class="instrument" x="296" y="444">Viola</text>
    <rect class="bar-high" x="582" y="437.5" width="246" height="5" rx="2.5"/><rect class="bar-low" x="312" y="437.5" width="272" height="5" rx="2.5"/></g>
  <g class="instrument-row"><text class="instrument" x="355" y="460">Violin</text>
    <rect class="bar-high" x="619" y="453.5" width="319" height="5" rx="2.5"/><rect class="bar-low" x="368" y="453.5" width="253" height="5" rx="2.5"/></g>
  <g class="instrument-row"><text class="instrument" x="243" y="475">Guitar</text>
    <rect class="bar-high" x="606" y="468.5" width="191" height="5" rx="2.5"/><rect class="bar-low" x="255" y="468.5" width="353" height="5" rx="2.5"/></g>
  <g class="instrument-row"><text class="instrument" x="98" y="491">Harp</text>
    <rect class="bar-high" x="734" y="484.5" width="82" height="5" rx="2.5"/><rect class="bar-low" x="113" y="484.5" width="623" height="5" rx="2.5"/></g>
  <g class="instrument-row"><text class="instrument after" x="868" y="506">Pipe Organ</text>
    <rect class="bar-low" x="64" y="499.5" width="786" height="5" rx="2.5"/></g>

  <g class="piano">
    <text class="piano-title" x="430" y="538">Standard 88-key Piano</text>
    <polyline class="bracket" points="100,548 100,534 360,534"/>
    <polyline class="bracket" points="500,534 778,534 778,548"/>
    <g role="img" aria-label="88-key piano keyboard spanning octaves 0 to 9, aligned to the frequency axis">
      <rect class="keyboard" x="36" y="551" width="907" height="39"/>
    </g>
    <line class="marker" x1="407" y1="590" x2="407" y2="602"/>
    <text class="marker-label" x="409" y="617">Middle C</text>
    <line class="marker" x1="478" y1="590" x2="478" y2="602"/>
    <text class="marker-label" x="478" y="611">A</text>
    <text class="marker-label" x="478" y="625">440</text>
  </g>

  <g class="tags">
    <g class="pill"><rect x="104" y="601" width="56" height="16" rx="8"/><text x="132" y="613">Rumble</text></g>
    <g class="pill"><rect x="64" y="629" width="84" height="16" rx="8"/><text x="106" y="641">Chest/Thump</text></g>
    <g class="pill"><rect x="219" y="621" width="46" height="16" rx="8"/><text x="242" y="633">Bottom</text></g>
    <g class="pill small"><rect x="190" y="649" width="45" height="15" rx="7.5"/><text x="212.5" y="659.5">AC/Ground</text></g>
    <g class="pill"><rect x="321" y="637" width="69" height="16" rx="8"/><text x="355.5" y="649">Warmth</text></g>
    <g class="pill"><rect x="282" y="666" width="70" height="16" rx="8"/><text x="317" y="678">Boom/Punch</text></g>
    <g class="pill"><rect x="395" y="654" width="85" height="16" rx="8"/><text x="437.5" y="666">Fullness/Mud</text></g>
    <g class="pill"><rect x="478" y="634" width="93" height="17" rx="8.5"/><text x="524.5" y="646.5">Honk</text></g>
    <g class="pill"><rect x="550" y="609" width="99" height="17" rx="8.5"/><text x="599.5" y="621.5">Whack</text></g>
    <g class="pill"><rect x="584" y="654" width="93" height="16" rx="8"/><text x="630.5" y="666">Tinny</text></g>
    <g class="pill"><rect x="669" y="620" width="88" height="16" rx="8"/><text x="713" y="632">Crunch</text></g>
    <g class="pill"><rect x="767" y="597" width="110" height="17" rx="8.5"/><text x="822" y="609.5">Sibilance</text></g>
    <g class="pill"><rect x="812" y="624" width="68" height="16" rx="8"/><text x="846" y="636">Definition</text></g>
    <g class="pill"><rect x="745" y="642" width="63" height="17" rx="8.5"/><text x="776.5" y="654.5">Edge</text></g>
    <g class="pill"><rect x="928" y="609" width="59" height="17" rx="8.5"/><text x="957.5" y="621.5">Air</text></g>
    <g class="pill"><rect x="864" y="650" width="42" height="16" rx="8"/><text x="885" y="662">Pierce</text></g>
    <g class="pill"><rect x="676" y="677" width="298" height="17" rx="8.5"/><text x="825" y="689.5">Treble</text></g>
  </g>

  <g class="axis thirds">
    <text class="axis-label" x="65" y="715">20</text>
    <text class="axis-label" x="97" y="715">25</text>
    <text class="axis-label" x="124" y="715">31.5</text>
    <text class="axis-label" x="165" y="715">40</text>
    <text class="axis-label" x="192" y="715">50</text>
    <text class="axis-label" x="236" y="715">63</text>
    <text class="axis-label" x="257" y="715">80</text>
    <text class="axis-label" x="283" y="715">100</text>
    <text class="axis-label" x="312" y="715">125</text>
    <text class="axis-label" x="338" y="715">160</text>
    <text class="axis-label" x="365" y="715">200</text>
    <text class="axis-label" x="397" y="715">250</text>
    <text class="axis-label" x="424" y="715">315</text>
    <text class="axis-label" x="464" y="715">400</text>
    <text class="axis-label" x="491" y="715">500</text>
    <text class="axis-label" x="527" y="715">630</text>
    <text class="axis-label" x="558" y="715">800</text>
    <text class="axis-label" x="582" y="715">1K</text>
    <text class="axis-label" x="614" y="715">1.25K</text>
    <text class="axis-label" x="645" y="715">1.6K</text>
    <text class="axis-label" x="675" y="715">2K</text>
    <text class="axis-label" x="703" y="715">2.5K</text>
    <text class="axis-label" x="735" y="715">3.15K</text>
    <text class="axis-label" x="763" y="715">4K</text>
    <text class="axis-label" x="791" y="715">5K</text>
    <text class="axis-label" x="827" y="715">6.3K</text>
    <text class="axis-label" x="852" y="715">8K</text>
    <text class="axis-label" x="884" y="715">10K</text>
    <text class="axis-label" x="912" y="715">12.5K</text>
    <text class="axis-label" x="942" y="715">16K</text>
    <text class="axis-label" x="970" y="715">20K</text>
  </g>

  <g class="bands">
    <line class="rule" x1="0" y1="723" x2="993" y2="723"/>
    <line class="rule" x1="0" y1="752" x2="993" y2="752"/>
    <text class="band-name" x="127" y="743">Sub Bass</text>
    <text class="band-name" x="309" y="744">Bass</text>
    <text class="band-name" x="538" y="745">Mid Range</text>
    <text class="band-name" x="746" y="743">High Mids</text>
    <text class="band-name" x="905" y="745">High Freqs</text>
  </g>

  <g class="axis bottom">
    <text class="axis-unit" x="18" y="771">Hz</text>
    <text class="axis-label" x="65" y="771">20</text>
    <text class="axis-label" x="165" y="771">40</text>
    <text class="axis-label" x="212" y="771">60</text>
    <text class="axis-label" x="283" y="771">100</text>
    <text class="axis-label" x="360" y="771">200</text>
    <text class="axis-label" x="464" y="771">400</text>
    <text class="axis-label" x="517" y="771">600</text>
    <text class="axis-label" x="585" y="771">1K</text>
    <text class="axis-label" x="679" y="771">2K</text>
    <text class="axis-label" x="767" y="771">4K</text>
    <text class="axis-label" x="818" y="771">6K</text>
    <text class="axis-label" x="882" y="771">10K</text>
    <text class="axis-label" x="940" y="771">16K</text>
    <text class="axis-label" x="972" y="771">20K</text>
  </g>
</svg>
</body>
</html>
```